Email Template for AI Website Builder Marketing Campaign

Update: All the designs submitted have too much content for an email template. I have attached a mockup example of a simplified design. Please follow this guideline to revise your design to be less "wordy" and have less content to optimize the delivery rate of the emails. I have also attached the images I used to create the mockup. Feel free to use these images for your revised designs.
Original Brief:
I need a catchy email template for my new AI Website Builder, WebQuilt.ai. The template must be professional, colorful, yet not too complex. The concept of the product is this:
WebQuilt uses Artificial Intelligence (AI) to instantly build stunning websites, absolutely FREE. The user simply specifies their business name and business category (industry), and their stunning new website appears before their eyes!
The template will be used in MailChimp, so please provide the code that I can simply paste into the email body.
Here is a screenshot of our new website (which is not online yet) so you can match the color scheme and style of the email template to the new website design:
https://pixbinstore.com/art_img/7310582/2208634/48165027/9qrt41hwk826zlmpb3nqd7wyex_image.jpg
Let me know if you have any questions.
Thanks!
All submitted designs are too lengthy (too much content) for an email template. I will provide a mockup showing a sample of how you can simplify your design to function better as an email template and better suit my needs. I appreciate your patience!

```html
<!DOCTYPE html>
<html lang="en">
<head>
<meta charset="utf-8">
<title>WebQuilt – AI Website Builder</title>
<link rel="stylesheet" href="https://fonts.googleapis.com/css2?family=Raleway:wght@400;500;700&family=Mulish:wght@400;500&display=swap">
<style>
  :root {
    --white: #ffffff;
    --ink: #2b2b2b;
    --body-grey: #555555;
    --accent: #1aa3e8;
    --accent-deep: #0a82d6;
    --wave-blue: #2bb3e6;
    --footer: #232325;
    --footer-bottom: #1b1b1c;
    --footer-text: #d8d8d8;
    --hero-dark: #4a4c55;
    --hero-mid: #8c8f98;
    --hero-light: #c9cbd0;
  }
  * { box-sizing: border-box; margin: 0; padding: 0; }
  html, body { width: 933px; height: 1200px; overflow: hidden; background: var(--white); }
  body { position: relative; font-family: "Mulish", Arial, sans-serif; }

  .hero { position: absolute; left: 0; top: 0; width: 933px; height: 580px; overflow: hidden; }
  .hero-photo {
    position: absolute; inset: 0;
    background: linear-gradient(100deg, var(--hero-dark) 0%, #6e7079 35%, var(--hero-mid) 55%, var(--hero-light) 75%, #9a9ca3 100%);
  }
  .hero-wave { position: absolute; left: 0; bottom: 0; width: 933px; height: 60px; }

  .brand { position: absolute; display: flex; align-items: center; gap: 10px; }
  .brand-dot { width: 40px; height: 40px; border-radius: 50%; background: linear-gradient(135deg, #3fc1f0, var(--accent-deep)); }
  .brand-name { font-family: "Raleway", Arial, sans-serif; font-weight: 500; color: var(--white); }
  .hero .brand { left: 87px; top: 19px; }
  .hero .brand-name { font-size: 21px; }

  .hero-kicker { position: absolute; left: 87px; top: 135px; font-size: 17px; color: var(--white); }
  .hero-title { position: absolute; left: 87px; top: 168px; font-family: "Raleway", Arial, sans-serif; font-weight: 500; font-size: 27px; line-height: 43px; color: var(--white); }
  .hero-text { position: absolute; left: 87px; top: 274px; width: 310px; font-size: 16px; line-height: 33px; color: var(--white); }
  .hero-button {
    position: absolute; left: 87px; top: 410px; width: 243px; height: 62px; border-radius: 31px;
    background: linear-gradient(180deg, var(--accent) 0%, var(--accent-deep) 100%);
    color: var(--white); font-size: 17px; display: flex; align-items: center; justify-content: center;
    text-transform: uppercase;
  }

  .feature-visual {
    position: absolute; left: 87px; top: 628px; width: 386px; height: 232px; border-radius: 10px 10px 4px 4px;
    background: linear-gradient(135deg, #3a1b6e 0%, #5a2aa0 50%, #2a1556 100%);
    border: 10px solid #1a1a1d; border-bottom-width: 14px;
  }
  .feature-label { position: absolute; left: 490px; top: 646px; font-size: 17px; color: var(--accent); }
  .feature-title { position: absolute; left: 490px; top: 668px; font-family: "Raleway", Arial, sans-serif; font-weight: 400; font-size: 30px; color: var(--ink); }
  .feature-title strong { font-weight: 700; }
  .feature-text { position: absolute; left: 490px; top: 728px; width: 350px; font-size: 16px; line-height: 29px; color: var(--body-grey); }

  .footer { position: absolute; left: 0; top: 924px; width: 933px; height: 232px; background: var(--footer); }
  .footer .brand { left: 50%; top: 42px; transform: translateX(-50%); }
  .footer .brand-dot { width: 50px; height: 50px; }
  .footer .brand-name { font-size: 25px; }
  .footer-nav { position: absolute; left: 0; top: 118px; width: 933px; display: flex; justify-content: center; gap: 34px; font-size: 13px; color: var(--white); text-transform: uppercase; }
  .social { position: absolute; left: 0; top: 164px; width: 933px; display: flex; justify-content: center; gap: 9px; }
  .social span { width: 26px; height: 26px; border-radius: 50%; background: var(--white); }

  .legal { position: absolute; left: 0; top: 1156px; width: 933px; height: 44px; background: var(--footer-bottom); color: var(--footer-text); font-size: 11px; display: flex; align-items: center; justify-content: center; text-transform: uppercase; }
</style>
</head>
<body>
  <header class="hero">
    <div class="hero-photo" role="img" aria-label="Photo of a white humanoid robot typing at a desktop computer in a bright office"></div>
    <svg class="hero-wave" viewBox="0 0 933 60" preserveAspectRatio="none" aria-hidden="true">
      <path d="M0 40 C 180 0, 380 0, 520 20 C 680 44, 820 52, 933 44 L933 60 L0 60 Z" fill="var(--wave-blue)"/>
      <path d="M0 60 L0 50 C 180 8, 380 6, 520 26 C 680 50, 820 58, 933 56 L933 60 Z" fill="var(--white)"/>
    </svg>
    <div class="brand"><span class="brand-dot"></span><span class="brand-name">WebQuilt</span></div>
    <p class="hero-kicker">Let Artificial Intelligence</p>
    <h1 class="hero-title">Build Your Stunning<br>Website Instanly</h1>
    <p class="hero-text">Sed ut perspiciatis unde omnis iste natus error sit voluptatem accusantium doloremque laudantium</p>
    <a class="hero-button">Build my free website</a>
  </header>

  <section class="feature">
    <div class="feature-visual" role="img" aria-label="Laptop showing a purple illustration of an AI chip surrounded by circuit lines and devices"></div>
    <p class="feature-label">AI Website Generator</p>
    <h2 class="feature-title">Build a Website <strong>with AI</strong></h2>
    <p class="feature-text">Sed ut perspiciatis unde omnis iste natus error sit voluptatem accusantium doloremque laudantium, totam rem aperiam, eaque ipsa quae ab illo inventore...</p>
  </section>

  <footer class="footer">
    <div class="brand"><span class="brand-dot"></span><span class="brand-name">WebQuilt</span></div>
    <nav class="footer-nav">
      <span>About WebQuilt</span><span>About AI</span><span>History of AI</span><span>Make Money Quilt</span>
    </nav>
    <div class="social" aria-label="Social links">
      <span></span><span></span><span></span><span></span><span></span><span></span>
    </div>
  </footer>
  <div class="legal">Copyright © 2023 | Privacy Policy</div>
</body>
</html>
```